Crumbwell Courier The Next Generation

we have a website www.crumbwellcourier.ae which needs a complete graphical overhaul.
We are a bakery in Dubai, producing artisan breads and related products. Also salads and sandwiches. All fresh, all handmade, best quality.
We'd like to have something that looks fresh, modern, nice colours (no dark colours). Trendy but still transporting the feeling of the "good ol' bakery).
Our customers are expats, mostly english speakers. But we'd like to attract more different nationalities!
Also, customers are individuals and also companies (offices, airlines, yacht charters...) The third section are coffee shops, restaurants, hotels....
We have also an online shop. This is a MUST and can be optimised.
We'd like to stick with wordpress and woocommerce.
It MUST be responsive and easy to navigate on mobile devices. 60% of our customers order on mobile phones... browsing is even more.

Bakery

```html
<!DOCTYPE html>
<html lang="en">
<head>
<meta charset="utf-8">
<title>Crumbwell Courier – Artisan Bakery</title>
<link href="https://fonts.googleapis.com/css2?family=Open+Sans:wght@400;600;700&family=Courgette&display=swap" rel="stylesheet">
<style>
:root{
  --green:#5e7d2c;
  --orange:#f1a23a;
  --ink:#333333;
  --muted:#8a8a8a;
  --topbar:#3b3b3b;
  --footer:#2f2f2f;
  --footer-bottom:#232323;
  --soft:#f1f1f1;
  --hero:#ececec;
  --tan:#c9a877;
  --brown:#8c6a3c;
  --crust:#b9803f;
  --crumb:#e3c38c;
  --white:#ffffff;
}
*{box-sizing:border-box;margin:0;padding:0}
html,body{width:1200px;height:2964px;overflow:hidden}
body{font-family:"Open Sans",Arial,sans-serif;color:var(--ink);background:var(--white)}
a{color:inherit;text-decoration:none}

.topbar{height:40px;background:var(--topbar);color:#ddd;font-size:12px;display:flex;align-items:center;padding:0 64px;gap:28px}
.topbar .item{display:flex;align-items:center;gap:8px}
.topbar .search{margin-left:auto;display:flex;align-items:center;gap:10px}
.topbar .search span{display:block;width:150px;height:22px;border-bottom:1px solid #777;color:#999;line-height:22px}

.header{height:136px;display:flex;align-items:center;padding:0 64px;position:relative}
.tagline{font-size:13px;font-style:italic;width:330px}
.brand{position:absolute;left:50%;top:18px;transform:translateX(-50%);width:210px;height:100px;background:var(--tan);border:3px solid var(--brown);display:flex;align-items:center;justify-content:center;gap:10px}
.brand .dot{width:14px;height:14px;background:#5a3d1c}
.brand .name{font-weight:700;font-size:18px;color:#5a3d1c;text-align:center;line-height:1.15}
.hours{margin-left:auto;display:flex;align-items:center;gap:10px;font-size:13px}
.hours b{display:block;font-weight:600}

.nav{height:56px;background:var(--green);display:flex;align-items:center;justify-content:center;gap:64px;color:var(--white);font-size:15px}

.hero{height:428px;background:linear-gradient(180deg,#f6f6f6,var(--hero));position:relative;overflow:hidden}
.hero h1{position:absolute;left:120px;top:100px;font-family:"Courgette",cursive;font-weight:400;font-size:46px;color:var(--orange)}
.btn-dark{position:absolute;left:126px;top:188px;background:var(--topbar);color:var(--white);font-size:15px;padding:13px 30px;border-radius:3px}
.hero-photo{position:absolute;left:690px;top:30px;width:340px;height:300px;border-radius:6px;background:linear-gradient(160deg,var(--crumb) 0%,#c99455 55%,#a06a32 100%)}
.hero-base{position:absolute;left:650px;top:330px;width:420px;height:70px;background:var(--white);box-shadow:0 6px 14px rgba(0,0,0,.08)}
.hero .arrow{position:absolute;top:202px}

.section-title{text-align:center;font-size:30px;font-weight:700;color:#444}
.section-title::after{content:"";display:block;width:60px;height:2px;background:var(--green);margin:14px auto 0}

.services{height:480px;padding-top:68px}
.service-list{display:flex;justify-content:center;gap:45px;margin-top:56px}
.service{width:180px;text-align:center;font-size:14px;color:#555;white-space:nowrap}
.service .ring{width:144px;height:144px;border:3px solid var(--brown);border-radius:50%;margin:0 auto 20px;display:flex;align-items:center;justify-content:center}
.service .ring svg{display:block}
.service.active{color:var(--green);font-weight:700}

.products{height:900px;background:var(--soft);padding-top:40px}
.product-grid{position:relative;width:1056px;margin:68px auto 0;display:grid;grid-template-columns:1fr 1fr;column-gap:88px;row-gap:68px}
.product-grid::after{content:"";position:absolute;left:527px;top:0;width:2px;height:100%;background:#cfcfcf}
.product{display:flex;gap:26px;height:172px}
.product .photo{width:176px;height:140px;flex:none;display:flex;align-items:center;justify-content:center}
.product .photo i{display:block}
.product .info{flex:1;padding-top:10px}
.product .row{display:flex;justify-content:space-between;align-items:baseline;padding-right:20px}
.product h3{font-size:26px;font-weight:600;color:#3a3a3a}
.product .price{color:var(--orange);font-size:15px}
.product .range{font-size:11px;color:var(--muted);margin-top:4px}
.btn-outline{display:inline-block;margin-top:16px;border:2px solid #444;padding:7px 22px;font-size:12px;font-weight:700}

.boxes{height:560px;padding-top:50px;position:relative}
.box-panel{position:absolute;left:440px;top:158px;width:680px;height:344px;background:var(--orange);color:var(--white);padding:38px 0 0 160px}
.box-panel h3{font-size:30px;font-weight:400}
.box-panel .amount{font-size:28px;font-weight:700;margin-top:22px}
.box-panel p{font-size:14px;line-height:1.5;margin-top:10px;width:460px}
.btn-black{display:inline-block;margin-top:26px;background:#111;color:var(--white);font-size:13px;font-weight:700;padding:12px 26px}
.box-photo{position:absolute;left:64px;top:190px;width:520px;height:290px;border-radius:6px;background:linear-gradient(160deg,var(--crumb) 0%,#c38a4a 60%,#9a6630 100%);box-shadow:0 8px 18px rgba(0,0,0,.12)}

.footer{height:320px;background:var(--footer);color:#cfcfcf;padding:46px 80px 0 76px;display:grid;grid-template-columns:314px 210px 240px 1fr;font-size:12px}
.footer h4{color:var(--white);font-size:17px;font-weight:600;margin-bottom:26px;height:24px}
.footer li{list-style:none;margin-bottom:11px;display:flex;gap:10px;align-items:flex-start}
.footer .bullet{color:var(--green);font-weight:700}
.map{width:100%;height:170px;background:linear-gradient(135deg,#ebe7df,#d3dccb)}
.bottom{height:44px;background:var(--footer-bottom);color:#aaa;font-size:12px;display:flex;align-items:center;padding:0 80px}
.bottom .social{margin-left:auto;display:flex;gap:14px}
.bottom .social i{width:14px;height:14px;border-radius:50%;background:#888;display:block}
</style>
</head>
<body>

<div class="topbar">
  <div class="item"><svg width="14" height="10" viewBox="0 0 14 10"><rect x="0.5" y="0.5" width="13" height="9" fill="none" stroke="#ddd"/><path d="M1 1l6 5 6-5" fill="none" stroke="#ddd"/></svg>hello@crumbwellcourier.ae</div>
  <div class="item"><svg width="12" height="12" viewBox="0 0 12 12"><path d="M3 1l2 3-1 1c1 2 2 3 3 3l1-1 3 2-1 2C5 11 1 7 1 2z" fill="#ddd"/></svg>+971 4 555 0192</div>
  <div class="search"><span>Search...</span><svg width="14" height="14" viewBox="0 0 14 14"><circle cx="6" cy="6" r="4.5" fill="none" stroke="#ddd" stroke-width="1.6"/><path d="M9.5 9.5L13 13" stroke="#ddd" stroke-width="1.6"/></svg></div>
</div>

<header class="header">
  <p class="tagline">"Your bakery, where everything is h... handmade"</p>
  <div class="brand"><span class="dot"></span><span class="name">Crumbwell<br>Courier</span></div>
  <div class="hours">
    <svg width="24" height="24" viewBox="0 0 24 24"><circle cx="12" cy="12" r="10" fill="none" stroke="#333" stroke-width="2"/><path d="M12 6v6l4 3" fill="none" stroke="#333" stroke-width="2"/></svg>
    <div><b>Opening hours:</b>Sun - Thu 07:00 - 15:00</div>
  </div>
</header>

<nav class="nav">
  <a href="#">Home</a><a href="#">About us</a><a href="#">Our menu</a><a href="#">Our boxes</a><a href="#">Great British Pies</a><a href="#">Delivery</a>
</nav>

<section class="hero">
  <svg class="arrow" style="left:24px" width="14" height="24" viewBox="0 0 14 24"><path d="M12 2L2 12l10 10" fill="none" stroke="#bbb" stroke-width="3"/></svg>
  <h1>Freshly Baked Everyday</h1>
  <a class="btn-dark" href="#">View More</a>
  <div class="hero-base"></div>
  <div class="hero-photo" role="img" aria-label="Three artisan loaves standing upright on a white board with herbs"></div>
  <svg class="arrow" style="right:24px" width="14" height="24" viewBox="0 0 14 24"><path d="M2 2l10 10L2 22" fill="none" stroke="#bbb" stroke-width="3"/></svg>
</section>

<section class="services">
  <h2 class="section-title">Main Services We Provided</h2>
  <div class="service-list">
    <div class="service"><div class="ring"><svg width="70" height="46" viewBox="0 0 70 46"><rect x="2" y="6" width="66" height="34" rx="17" fill="#8a8a8a"/></svg></div>Breads, buns and more</div>
    <div class="service"><div class="ring"><svg width="64" height="46" viewBox="0 0 64 46"><path d="M4 20h56l-6 22H10z" fill="#8a8a8a"/><path d="M4 20a28 14 0 0 1 56 0z" fill="#a5a5a5"/></svg></div>Great British Pies</div>
    <div class="service active"><div class="ring"><svg width="70" height="46" viewBox="0 0 70 46"><path d="M6 30L34 10l30 20z" fill="#3f5a1c"/><rect x="6" y="30" width="58" height="8" fill="#5e7d2c"/></svg></div>Sandwich Platters</div>
    <div class="service"><div class="ring"><svg width="64" height="50" viewBox="0 0 64 50"><path d="M6 22a26 18 0 0 1 52 0z" fill="#8a8a8a"/><rect x="4" y="26" width="56" height="6" rx="3" fill="#a5a5a5"/><rect x="6" y="36" width="52" height="8" rx="4" fill="#8a8a8a"/></svg></div>Finger foods</div>
    <div class="service"><div class="ring"><svg width="70" height="46" viewBox="0 0 70 46"><path d="M4 16h62a31 28 0 0 1-62 0z" fill="#8a8a8a"/></svg></div>Salads</div>
  </div>
</section>

<section class="products">
  <h2 class="section-title">Our product</h2>
  <div class="product-grid">
    <div class="product"><div class="photo" role="img" aria-label="Round focaccia bread"><i style="width:132px;height:132px;border-radius:50%;background:radial-gradient(circle at 45% 40%,#ecd08a,#c8993e)"></i></div><div class="info"><div class="row"><h3>Focaccia</h3><span class="price">$20.00</span></div><p class="range">2.00 AED – 12.00 AED</p><a class="btn-outline" href="#">ORDER NOW</a></div></div>
    <div class="product"><div class="photo" role="img" aria-label="Sliced white loaf"><i style="width:170px;height:110px;border-radius:50px 50px 14px 14px;background:linear-gradient(180deg,#d28f46,#f0d3a0)"></i></div><div class="info"><div class="row"><h3>Hi-Top</h3><span class="price">$20.00</span></div><p class="range">4.00 AED – 9.00 AED</p><a class="btn-outline" href="#">ORDER NOW</a></div></div>
    <div class="product"><div class="photo" role="img" aria-label="Ring-shaped pie"><i style="width:132px;height:132px;border-radius:50%;border:36px solid #c8894a;background:transparent"></i></div><div class="info"><div class="row"><h3>Ring pie</h3><span class="price">$20.00</span></div><p class="range">90.00 AED – 15.00 AED</p><a class="btn-outline" href="#">ORDER NOW</a></div></div>
    <div class="product"><div class="photo" role="img" aria-label="Cottage pie in a dish"><i style="width:170px;height:136px;border-radius:6px;background:linear-gradient(135deg,#9a6a3a,#6e4523)"></i></div><div class="info"><div class="row"><h3>Cottage Pie</h3><span class="price">$20.00</span></div><p class="range">15.00 AED</p><a class="btn-outline" href="#">ORDER NOW</a></div></div>
    <div class="product"><div class="photo" role="img" aria-label="Platter of classic cut sandwiches"><i style="width:170px;height:136px;border-radius:6px;background:linear-gradient(135deg,#cfc8b6,#8a9466)"></i></div><div class="info"><div class="row"><h3>Classic Cut</h3><span class="price">$20.00</span></div><p class="range">90.00 AED – 145.00 AED</p><a class="btn-outline" href="#">ORDER NOW</a></div></div>
    <div class="product"><div class="photo" role="img" aria-label="Bowl of Greek salad"><i style="width:150px;height:120px;border-radius:50%;background:radial-gradient(circle at 50% 40%,#8fbf4a,#5f8f2e)"></i></div><div class="info"><div class="row"><h3>Greek Salad</h3><span class="price">$20.00</span></div><p class="range">12.00 AED – 17.00 AED</p><a class="btn-outline" href="#">ORDER NOW</a></div></div>
  </div>
</section>

<section class="boxes">
  <h2 class="section-title">Selection Boxes</h2>
  <div class="box-panel">
    <h3>Couples Box</h3>
    <p class="amount">90.00 AED</p>
    <p>One pain campagne, 1 small brown sliced loaf, 1 small white sliced loaf, 4 brown rolls, 4 fresh buns, 2 croissants and 2 danish, 2 fruit pastries.</p>
    <a class="btn-black" href="#">ADD TO CART</a>
  </div>
  <div class="box-photo" role="img" aria-label="Basket of assorted breads, rolls and pastries on a wooden board"></div>
</section>

<footer class="footer">
  <div>
    <h4>Contact</h4>
    <ul>
      <li><span class="bullet">•</span><span>Crumbwell Courier Bakery<br>Unit 7, Bakers Lane, Al Quoz, Dubai</span></li>
      <li><span class="bullet">•</span>+971 4 555 0192</li>
      <li><span class="bullet">•</span>hello@crumbwellcourier.ae</li>
      <li><span class="bullet">•</span>Opening hours Sun - Thu 07:00 - 15:00</li>
    </ul>
  </div>
  <div>
    <h4>Quick Links</h4>
    <ul>
      <li><span class="bullet">›</span>Home</li><li><span class="bullet">›</span>About us</li><li><span class="bullet">›</span>Our menu</li><li><span class="bullet">›</span>Our boxes</li><li><span class="bullet">›</span>Great British Pies</li><li><span class="bullet">›</span>Delivery</li>
    </ul>
  </div>
  <div>
    <h4></h4>
    <ul>
      <li><span class="bullet">›</span>Standard terms</li><li><span class="bullet">›</span>Terms and Conditions</li><li><span class="bullet">›</span>Privacy</li>
    </ul>
  </div>
  <div>
    <h4>Location</h4>
    <div class="map" role="img" aria-label="Map showing the bakery location in Dubai"></div>
  </div>
</footer>
<div class="bottom">
  <span>© 2017. All rights reserved</span>
  <div class="social"><i></i><i></i><i></i><i></i></div>
</div>

</body>
</html>
```